Digital One Pager for Consulting Practice

I would like the essence of the content in my ppt consolidated into a one-pager. The one-pager will mainly be sent via email as a pdf and intended to excite and invite new clients and establish the credibility of my boutique high-end consulting firm. Infographics and symbols would be a plus. The target client should view the firm as providing premeir service. The client is getting a thought partner.

Target Market(s)

Large Medical Device Manufacturer Executives, Early-Stage Medical Device Manufacturer Executives, Partners at VC Firms

Industry/Entity Type

Medical Equipment

Colors
0355a3
f37122

Requirements
Must have
• Please match the color scheme in ppt. Please use the existing logo. I am very open to better graphics on the process. My photo does not need to be on the digital flyer. Hyper link to the website and email is needed.
Nice to have
• Infographics

```html
<!DOCTYPE html>
<html lang="en">
<head>
<meta charset="utf-8">
<title>Halden Ventures – Regulatory Support One-Pager</title>
<link href="https://fonts.googleapis.com/css2?family=Open+Sans:wght@400;600;700&family=Tinos:ital,wght@0,400;0,700;1,700&display=swap" rel="stylesheet">
<style>
  :root {
    --navy: #0e1b33;
    --navy-deep: #0b1a30;
    --orange: #f37122;
    --blue: #0355a3;
    --ink: #1c1c1c;
    --white: #ffffff;
    --circle-edge: #7fd1a4;
    --serif: "Tinos", "Times New Roman", serif;
    --sans: "Open Sans", Arial, sans-serif;
  }
  * { box-sizing: border-box; margin: 0; padding: 0; }
  html, body { width: 1007px; height: 1200px; overflow: hidden; background: var(--white); }
  .page { position: relative; width: 1007px; height: 1200px; font-family: var(--sans); color: var(--ink); }
  .abs { position: absolute; }

  /* Header */
  .hero { left: 0; top: 0; width: 1007px; height: 280px; }
  .hero-title { left: 0; top: 84px; width: 1007px; text-align: center; color: var(--white);
    font-family: var(--serif); font-size: 52px; line-height: 64px; font-weight: 400; }

  /* Experience */
  .section-heading { font-family: var(--serif); font-weight: 700; font-size: 31px; letter-spacing: .5px; }
  .experience-heading { left: 65px; top: 300px; color: var(--navy); }
  .bullet-list { list-style: none; font-size: 15.5px; line-height: 20px; }
  .bullet-list li { position: relative; padding-left: 23px; }
  .bullet-list li::before { content: ""; position: absolute; left: 0; top: 5px; width: 10px; height: 10px;
    border-radius: 50%; background: var(--orange); }
  .experience-list { left: 65px; top: 350px; width: 560px; }
  .experience-list li { margin-bottom: 14px; }
  .experience-list li.tight { margin-bottom: 0; }
  .venn { left: 598px; top: 292px; width: 370px; height: 280px; overflow: visible; }

  /* Services band */
  .services-band { left: 0; top: 582px; width: 1007px; height: 298px; }
  .services-heading { left: 65px; top: 592px; color: var(--white); }
  .svc-title { font-family: var(--serif); font-weight: 700; font-size: 18px; color: var(--navy); }
  .svc-list { list-style: none; font-size: 15px; line-height: 19px; color: var(--white); }
  .svc-list li { position: relative; padding-left: 17px; }
  .svc-list li::before { content: ""; position: absolute; left: 0; top: 5px; width: 9px; height: 9px;
    border-radius: 50%; background: var(--white); }

  .provide-heading { left: 600px; top: 595px; color: var(--white); font-size: 29px; }
  .provide-title { font-family: var(--serif); font-weight: 700; font-size: 18px; color: var(--orange); }
  .provide-list { list-style: none; font-size: 15px; line-height: 19px; color: var(--white); }
  .provide-list li { position: relative; padding-left: 17px; margin-bottom: 12px; }
  .provide-list li::before { content: ""; position: absolute; left: 0; top: 5px; width: 9px; height: 9px;
    border-radius: 50%; background: var(--white); }

  /* Process */
  .process-band { left: 0; top: 896px; width: 1007px; height: 168px; background: var(--navy-deep); }
  .process-heading { left: 65px; top: 908px; color: var(--white); font-size: 29px; }
  .process-flow { left: 45px; top: 958px; width: 915px; height: 88px; }
  .step-label { color: var(--white); font-weight: 600; font-size: 18px; line-height: 23px; }

  /* Footer */
  .brand { left: 55px; top: 1098px; display: flex; align-items: center; gap: 14px; }
  .brand-mark { width: 34px; height: 34px; background: var(--navy); }
  .brand-name { font-family: var(--sans); font-weight: 700; font-size: 34px; letter-spacing: 6px; color: var(--navy); line-height: 1; }
  .contact { right: 56px; top: 1078px; text-align: right; }
  .phone { font-family: var(--sans); font-weight: 700; font-size: 64px; line-height: 70px; color: var(--orange); letter-spacing: -1px; }
  .links { font-weight: 700; font-size: 16.5px; color: var(--ink); }
  .links a { color: var(--ink); text-decoration: none; }
</style>
</head>
<body>
<main class="page">

  <!-- Header -->
  <svg class="abs hero" viewBox="0 0 1007 280" aria-hidden="true">
    <path d="M0 0 H1007 V212 Q503 320 0 226 Z" fill="var(--navy)"/>
    <path d="M0 226 Q503 320 1007 212" fill="none" stroke="var(--orange)" stroke-width="6"/>
    <path d="M0 234 Q503 324 1007 220" fill="none" stroke="#111" stroke-width="3"/>
  </svg>
  <h1 class="abs hero-title">Regulatory support for medtech firms.<br>Diligence for investors.</h1>

  <!-- Experience -->
  <h2 class="abs section-heading experience-heading">EXPERIENCE:</h2>
  <ul class="abs bullet-list experience-list">
    <li>Over a decade &nbsp;@FDA (Former Deputy Division Director)</li>
    <li>Expertise: Cardiovascular, Ophthalmology, General<br>Hospital, Infection Control, Dental, Anesthesia, Respiratory</li>
    <li style="margin-bottom:20px">Vice President Regulatory Affairs / Quality Assurance @Corvane<br>(Fortune 150 Company)</li>
    <li class="tight">Initiated &nbsp;reorganization of department</li>
    <li class="tight">Led major compliance effort</li>
    <li class="tight">Successful FDA inspection (no observations)</li>
  </ul>

  <svg class="abs venn" viewBox="0 0 370 280" role="img" aria-label="Experience, Network and Process overlap to create Leverage">
    <defs>
      <linearGradient id="orb" x1="0" y1="0" x2="0" y2="1">
        <stop offset="0" stop-color="#d6d6d8"/>
        <stop offset="1" stop-color="#6f7075"/>
      </linearGradient>
    </defs>
    <circle cx="90" cy="86" r="84" fill="url(#orb)" stroke="var(--circle-edge)" stroke-width="2"/>
    <circle cx="274" cy="86" r="84" fill="url(#orb)" stroke="var(--circle-edge)" stroke-width="2"/>
    <circle cx="192" cy="192" r="84" fill="url(#orb)" stroke="var(--circle-edge)" stroke-width="2"/>
    <circle cx="184" cy="108" r="46" fill="#17345f"/>
    <g font-family="Tinos, serif" font-style="italic" font-weight="700" font-size="14" fill="#fff" text-decoration="underline" text-anchor="middle">
      <text x="80" y="91">Experience</text>
      <text x="286" y="91">Network</text>
      <text x="185" y="113">Leverage</text>
      <text x="187" y="215">Process</text>
    </g>
  </svg>

  <!-- Services band -->
  <svg class="abs services-band" viewBox="0 0 1007 298" aria-hidden="true">
    <rect width="1007" height="298" fill="var(--navy-deep)"/>
    <polygon points="0,0 530,0 567,298 0,298" fill="var(--orange)"/>
  </svg>
  <h2 class="abs section-heading services-heading">SERVICES:</h2>

  <div class="abs" style="left:65px; top:642px; width:270px;">
    <h3 class="svc-title">Regulatory Strategy</h3>
    <ul class="svc-list" style="margin-top:12px">
      <li>RAQA Organizational<br>Structure</li>
      <li style="margin-top:17px">Regulatory Pathway</li>
    </ul>
    <h3 class="svc-title" style="margin-top:12px">Interim Executive Leadership</h3>
    <ul class="svc-list" style="margin-top:6px">
      <li>Compliance Remediation</li>
      <li style="margin-top:17px">Accelerated Product<br>Registration</li>
    </ul>
  </div>

  <div class="abs" style="left:336px; top:640px; width:200px;">
    <h3 class="svc-title">FDA Communications</h3>
    <ul class="svc-list" style="margin-top:12px">
      <li>Deficiency Response</li>
      <li style="margin-top:17px">Application Review</li>
    </ul>
    <h3 class="svc-title" style="margin-top:22px">Training</h3>
    <ul class="svc-list" style="margin-top:6px">
      <li>FDA Communication</li>
      <li style="margin-top:17px">MDR Reporting</li>
    </ul>
  </div>

  <h2 class="abs section-heading provide-heading">Experience to Provide...</h2>
  <div class="abs" style="left:598px; top:640px; width:370px;">
    <h3 class="provide-title">Executive Application Review</h3>
    <ul class="provide-list" style="margin-top:12px">
      <li>Examples include: Presubmission, IDE, 510(k),<br>513(g), PMA, Refuse to Accept, Hold letter</li>
      <li>Troubleshooting</li>
    </ul>
    <h3 class="provide-title" style="margin-top:16px">Strategic Advice &amp; Diligence to Investors</h3>
    <ul class="provide-list" style="margin-top:10px">
      <li>Validate &amp; Verify Founder Milestones</li>
      <li>Diligence portfolio company Regulatory<br>and Quality systems</li>
    </ul>
  </div>

  <!-- Process -->
  <section class="abs process-band"></section>
  <h2 class="abs section-heading process-heading">Efficient Process</h2>
  <svg class="abs process-flow" viewBox="0 0 915 88" role="img" aria-label="Process: Exploratory Call, Regulatory Landscape, Problem Statement, Review and Align on Deliverables">
    <rect x="0" y="0" width="240" height="88" rx="22" fill="#4a78c2"/>
    <rect x="215" y="0" width="240" height="88" rx="22" fill="#3f6ebd"/>
    <rect x="430" y="0" width="240" height="88" rx="22" fill="#3466b8"/>
    <rect x="645" y="0" width="270" height="88" rx="22" fill="#1d4fa8"/>
    <rect x="0" y="0" width="28" height="88" fill="#4a78c2"/>
    <rect x="890" y="40" width="25" height="48" fill="#1d4fa8"/>
    <g fill="#fff">
      <circle cx="219" cy="44" r="15"/><circle cx="433" cy="44" r="15"/><circle cx="646" cy="44" r="15"/>
    </g>
    <g fill="none" stroke="#1d4fa8" stroke-width="2.5" stroke-linecap="round" stroke-linejoin="round">
      <path d="M211 44 H227 M221 38 L227 44 L221 50"/>
      <path d="M425 44 H441 M435 38 L441 44 L435 50"/>
      <path d="M638 44 H654 M648 38 L654 44 L648 50"/>
    </g>
  </svg>
  <div class="abs step-label" style="left:80px; top:978px;">Exploratory<br>Call</div>
  <div class="abs step-label" style="left:315px; top:978px;">Regulatory<br>Landscape</div>
  <div class="abs step-label" style="left:533px; top:978px;">Problem<br>Statement</div>
  <div class="abs step-label" style="left:735px; top:978px;">Review &amp; Align on<br>Deliverables</div>

  <!-- Footer -->
  <div class="abs brand">
    <span class="brand-mark"></span>
    <span class="brand-name">HALDEN VENTURES</span>
  </div>
  <div class="abs contact">
    <div class="phone">555.014.2287</div>
    <div class="links"><a href="mailto:info@haldenventures.com">info@haldenventures.com</a> | <a href="https://www.haldenventures.com">www.haldenventures.com</a></div>
  </div>

</main>
</body>
</html>
```